Native Bush Healing Balms/Oils needs label/logo

Kōwhai Ripples is our name, we are a new startup business in New Zealand. Kōwhai means love in Maori. We make native bush balms, oils, tinctures, teas and do mirimiri which is a form of Maori healing. We are wanting a design for a balm label first off, however keep in mind that we will be wanting to transfer the logo across to other products, like the teas, t-shirts and even a calico tote bag! We would like it so we can edit the ingredients if possible.

We have had the 'flower/heart logo' made up to replace the 'o' in kōwhai. This we would like in a metallic electric purple/violet colour. We would like the 'kōwhai ripples' in silver. Please make sure the macron is above the last ā in kōwhai. We are open to other colour options and other styles of the flower/heart logo.

We would like the overall effect to be simple, clean, minimalist, bright. Colours we like are electric purple/violet, silver, then thinking of different colours for the different types/flavours, probably on a matte sticker. Fonts we think will suit are an italic curved/rounded font for the kōwhai and a capital font for the vibrations.

We have had a quick mock up of the labels which is attached. Also attached is a photo of my current balm and teas, and label ideas that I like. The drawings show a sticker for the lid with a safety tab.

Looking forward to seeing your wonderful designs! :)

Target Market(s)

People into natural self healing, who want traditionally made high vibrational, top end products

Industry/Entity Type

Health And Wellness

Requirements
Must have
• Silver writing on logo, or front of jar or lid.
• 'Made in Aotearoa' on jar
Nice to have
• Colours I like are hot pink, yellow, bright teal green, royal purple
Should not have
• Should not be cluttered

```html
<!DOCTYPE html>
<html lang="en">
<head>
<meta charset="utf-8">
<title>Kōwhai Ripples – Kawakawa Handmade Balm Label</title>
<link rel="stylesheet" href="https://fonts.googleapis.com/css2?family=Arimo:wght@400;700&display=swap">
<style>
  :root {
    --backdrop: #ececec;
    --label-teal: #8fdcc7;
    --label-teal-light: #a9e6d6;
    --label-teal-deep: #72cfb6;
    --ink-green: #17844c;
    --ink-muted: #2f6b4e;
    --silver: #6e7b80;
    --grass-green: #5cbf3a;
    --grass-light: #9ddf6a;
  }
  * { box-sizing: border-box; margin: 0; padding: 0; }
  html, body {
    width: 1200px;
    height: 1200px;
    overflow: hidden;
    background: var(--backdrop);
    font-family: "Arimo", Arial, sans-serif;
  }
  .canvas { position: relative; width: 1200px; height: 1200px; }

  /* Lid sticker */
  .lid-sticker {
    position: absolute;
    left: 430px;
    top: 40px;
    width: 340px;
    height: 340px;
    border-radius: 50%;
    background: radial-gradient(circle at 50% 45%, var(--label-teal-light), var(--label-teal) 70%, var(--label-teal-deep));
    overflow: hidden;
    text-align: center;
    color: var(--ink-green);
  }
  .lid-blossoms {
    position: absolute; top: 0; left: 0; right: 0; height: 80px;
    background: linear-gradient(180deg, rgba(244,251,248,0.55), rgba(185,178,122,0.15) 70%, transparent);
  }
  .lid-grass {
    position: absolute; bottom: 0; left: 0; right: 0; height: 70px;
    background: linear-gradient(180deg, transparent, var(--grass-light) 55%, var(--grass-green));
  }
  .lid-content {
    position: absolute; inset: 0;
    display: flex; flex-direction: column; align-items: center; justify-content: center;
    gap: 6px;
  }
  .lid-brand { font-size: 28px; color: var(--silver); }
  .lid-product { font-size: 40px; }
  .lid-type { font-size: 16px; font-weight: 700; letter-spacing: 1px; color: var(--ink-muted); }
  .lid-volume { font-size: 14px; color: var(--ink-muted); }

  /* Wrap label */
  .jar-label {
    position: absolute;
    left: 50px; top: 420px;
    width: 1100px; height: 740px;
    background: linear-gradient(90deg, var(--label-teal-deep), var(--label-teal) 25%, var(--label-teal-light) 50%, var(--label-teal) 75%, var(--label-teal-deep));
    overflow: hidden;
    color: var(--ink-green);
    text-align: center;
  }
  .label-blossoms {
    position: absolute; top: 0; left: 0; right: 0; height: 190px;
    background: linear-gradient(180deg, rgba(244,251,248,0.5), rgba(185,178,122,0.18) 55%, transparent);
  }
  .label-grass {
    position: absolute; bottom: 0; left: 0; right: 0; height: 180px;
    background: linear-gradient(180deg, transparent, rgba(157,223,106,0.8) 40%, var(--grass-green));
  }
  .label-brand {
    position: absolute; top: 130px; left: 0; right: 0;
    display: flex; align-items: center; justify-content: center; gap: 22px;
  }
  .label-brand-mark { width: 46px; height: 46px; border-radius: 50%; background: var(--silver); }
  .label-brand-name { font-size: 88px; font-weight: 400; line-height: 1; color: var(--silver); }
  .label-rule {
    position: absolute; top: 250px; left: 300px; right: 300px;
    height: 3px; background: var(--silver);
  }
  .label-product {
    position: absolute; top: 330px; left: 0; right: 0;
    font-size: 110px; font-weight: 400; line-height: 1;
  }
  .label-type {
    position: absolute; top: 470px; left: 0; right: 0;
    font-size: 34px; font-weight: 700; letter-spacing: 2px; color: var(--ink-muted);
  }
  .label-origin {
    position: absolute; top: 540px; left: 0; right: 0;
    font-size: 26px; font-weight: 700; letter-spacing: 3px; text-transform: uppercase;
    color: var(--silver);
  }
  .label-volume {
    position: absolute; top: 640px; left: 0; right: 0;
    font-size: 28px; color: #24502e;
  }
</style>
</head>
<body>
  <main class="canvas">
    <section class="lid-sticker" aria-label="Lid sticker">
      <div class="lid-blossoms" role="img" aria-label="White blossoms on golden branches"></div>
      <div class="lid-grass" role="img" aria-label="Green grass along the edge"></div>
      <div class="lid-content">
        <p class="lid-brand">kōwhai ripples</p>
        <p class="lid-product">Kawakawa</p>
        <p class="lid-type">Handmade Balm</p>
        <p class="lid-volume">15 ml</p>
      </div>
    </section>

    <section class="jar-label" aria-label="Jar wrap label">
      <div class="label-blossoms" role="img" aria-label="White blossoms hanging from golden branches"></div>
      <div class="label-grass" role="img" aria-label="Bright green grass growing along the bottom"></div>
      <div class="label-brand">
        <span class="label-brand-mark" aria-hidden="true"></span>
        <h1 class="label-brand-name">kōwhai ripples</h1>
      </div>
      <div class="label-rule" aria-hidden="true"></div>
      <h2 class="label-product">Kawakawa</h2>
      <p class="label-type">Handmade Balm</p>
      <p class="label-origin">Made in Aotearoa</p>
      <p class="label-volume">15 ml</p>
    </section>
  </main>
</body>
</html>
```